Book cover for a very impressive real-life healing story from a stage IV deadly disease

I need a book cover design for the French translation of the US book http://www.brelvantbooks.example/Linders-Journey-Through-Illness-Story/dp/0412298765/ref=sr_1_4?s=books&ie=UTF8&qid=1455100794&sr=1-4&keywords=tam+vesko
.
I do not want the word AIDS on the French cover, as the story of this book applies to any disease.

The french title will be something like :
Un matin nouveau !
Condamné par la médecine, il guérit grâce au jeûne, la détoxination, et l’amour.

which means something like
A new morning!
Subtitle : Given up by official medecine, he managed to heal with fasting, detox and love.

Many thanks !

Target Market(s)

Anybody interested in natural health

Requirements
Must have
• Nothing special
Nice to have
• Nothing special
Should not have
• Nothing special

```html
<!DOCTYPE html>
<html lang="fr">
<head>
<meta charset="utf-8">
<title>Un matin nouveau ! — couverture</title>
<link rel="stylesheet" href="https://fonts.googleapis.com/css2?family=Bodoni+Moda:opsz,wght@6..96,400;6..96,500&display=swap">
<style>
  :root {
    --page-bg: #ffffff;
    --tone-sky: #7d8ea6;
    --tone-warm: #c9a27a;
    --tone-amber: #b98a5c;
    --tone-sea: #5e5248;
    --tone-shore: #2e2a27;
    --title-ink: #0c0c0c;
    --subtitle-ink: #ffffff;
  }
  * { margin: 0; padding: 0; box-sizing: border-box; }
  html, body {
    width: 1200px;
    height: 1200px;
    overflow: hidden;
    background: var(--page-bg);
  }
  .cover {
    position: absolute;
    left: 226px;
    top: 0;
    width: 749px;
    height: 1200px;
    overflow: hidden;
  }
  .cover-photo {
    position: absolute;
    inset: 0;
    background: linear-gradient(to bottom,
      var(--tone-sky) 0%,
      var(--tone-warm) 35%,
      var(--tone-amber) 52%,
      var(--tone-sea) 72%,
      var(--tone-shore) 100%);
  }
  .title {
    position: absolute;
    left: 0;
    width: 100%;
    font-family: "Bodoni Moda", "Didot", serif;
    font-weight: 500;
    color: var(--title-ink);
    text-align: center;
    line-height: 1;
    letter-spacing: -6px;
  }
  .title-line { display: block; }
  .title-line--first { font-size: 176px; margin-top: 52px; }
  .title-line--second { font-size: 170px; margin-top: -2px; }
  .subtitle {
    position: absolute;
    left: 40px;
    right: 20px;
    top: 1083px;
    font-family: "Bodoni Moda", "Didot", serif;
    font-weight: 400;
    font-size: 32px;
    line-height: 0.9;
    letter-spacing: -1.8px;
    color: var(--subtitle-ink);
    white-space: nowrap;
  }
</style>
</head>
<body>
  <main class="cover">
    <div class="cover-photo" role="img" aria-label="Photographie : silhouette d'un homme sautant de joie, bras ouverts, sur une plage au coucher du soleil"></div>
    <h1 class="title">
      <span class="title-line title-line--first">Un matin</span>
      <span class="title-line title-line--second">nouveau !</span>
    </h1>
    <p class="subtitle">Condamné par la médecine, il guérit grâce au jeûne,<br>la détoxination, et l’amour.</p>
  </main>
</body>
</html>
```